One of Australia's fastest growing energy maintenance contractors needs a new website

www.panelbrite.com.au
Our business has evolved over the past years and now our website is no longer relevant.
We clean solar panels and we vacuum roof gutters.
We clean solar panels on the roofs of residential houses right up to billion dollar solar farms with in excess of 1 million panels. We offer thermal image testing and bird proofing for our residential and commercial clients and thermal drone imaging services for our solar farm clients.
We vacuum clean roof gutters (using a LoftSuk) on the residential house next door right up to enormous private and public schools, colleges, shopping centres, strat complexes and commercial buildings.
When first built our business had more of a domestic residential skew and the website reflected that. While that is still part of our core business we are now bidding on and have secured large government, commercial and infrastructure contracts and our new website needs to reflect our growth and our new business. We need a new site that it optimised for both desktop ad phone viewing as our latest figures showed that 73% of people visiting our site are on mobile phones. We have an extensive amount of data on Trekmetrics available as well as Bidlinks. Both that would also need integrating with the site along with a few other plugins such as Kembo Chat IQ, Friendwall etc along with SEO key words etc. We are also the winner and finalists over multiple years of the small business of the year awards and we like to proudly and prominently display those on our site.
We are looking for a new site with a modern professional feel / theme
There is a definitive break in our business between the solar Panel cleaning clients and the gutter cleaning clients so we would like a home page that begins with a simple choice:
Solar Panel Cleaning – Gutter Cleaning
With a professional full screen background image (we have hundreds to choose from) and along the bottom a small area with rights reserved etc, phone number etc (at some point in the future we will split these into two businesses but for now it’s what we have).
After that selection is made we would like a repeat of that same scenario but the selection is:
If it’s Solar Panel Cleaning
(new background image)
Government – Infrastructure – Commercial – Residential
If it’s Gutter Cleaning
(new background image)
Government – Strata – Commercial – Residential
After making those choices then onto the relevant pages with background images relevant to each sector and a them that suits (on the residential we would like to keep the link to our trekmetrics reviews) - We will provide copy / text for each relevant page.
Other than that, a menu inclusive of the above and:
Resellers Portal – we will provide a link to this from Kembo CRM)
Customer portal (we will supply a link to this from our booking system)
We also need a page for our Solar Resellers / Partners page but we will give them a link to this, it won’t be listed on the site.
Request a quote page (Again we will provide information from Kembo as this will be linked to the CRM)
Standard contact us page inclusive of phone numbers, address and fields supplied from CRM
Sydney – 02 7391 5084
Southern Highlands – 02 4863 1507
Goulburn – 02 4863 1507
Canberra – 02 6178 3045
Wollongong – 02 4239 7615
sales@panelbrite.com.au
Head Office - Ferndell NSW 2583
ABN: 48762093115
Responsive Design: Optimized for desktop and mobile (73% mobile visitors).
Fast Loading Speed: Optimized for performance.
Smooth Transition Animations: For service and category selection.
Sticky Contact Bar: Always accessible at the bottom of mobile screens for quick calls.
SEO Optimization: Focused on government tenders, large-scale commercial contracts, and infrastructure projects.
Integrations
Trekmetrics & Trekmetrics Bidlinks.
Kembo Chat IQ.
Friendwall Beacon.
SEO tools and keyword optimization.
Many many more images available if needed

```html
<!DOCTYPE html>
<html lang="en">
<head>
<meta charset="utf-8">
<title>PanelBrite – Solar Panel Cleaning</title>
<link rel="stylesheet" href="https://fonts.googleapis.com/css2?family=Poppins:wght@400;500;600;700&display=swap">
<style>
:root{
  --blue:#0a6fc2;
  --blue-bright:#1b86e0;
  --navy:#0d1b33;
  --ink:#0b1526;
  --text:#36404f;
  --muted:#6b7686;
  --light:#eef3f8;
  --line:#d9e2ec;
  --white:#fff;
  --gold:#f5a623;
}
*{box-sizing:border-box;margin:0;padding:0}
html,body{width:1200px;height:4948px;overflow:hidden}
body{font-family:"Poppins",sans-serif;color:var(--text);background:var(--white);position:relative}
section,header,footer{position:relative;width:1200px;overflow:hidden}
.btn{display:inline-flex;align-items:center;gap:10px;background:var(--blue);color:var(--white);font-weight:600;font-size:17px;letter-spacing:.5px;padding:0 26px;height:48px;border-radius:4px;text-transform:uppercase}
.btn-outline{background:var(--white);color:var(--blue);border:2px solid var(--blue)}
.eyebrow{font-size:16px;font-weight:500;color:var(--ink);text-align:center}
.title{font-size:50px;font-weight:700;color:var(--blue);text-align:center;line-height:1.15}
.brand{display:flex;align-items:center;gap:12px;font-weight:700;font-size:30px}
.brand-dot{width:34px;height:34px;border-radius:50%}

/* HERO */
.hero{height:840px;background:linear-gradient(120deg,#1d3452 0%,#3b5a7a 45%,#8aa6bf 100%)}
.hero-photo{position:absolute;inset:0;background:linear-gradient(110deg,rgba(13,27,51,.85) 0%,rgba(13,27,51,.35) 55%,rgba(150,170,190,.2) 100%)}
.topbar{position:absolute;top:14px;right:30px;display:flex;gap:34px;font-size:15px;color:var(--white)}
.topbar span{display:flex;align-items:center;gap:8px}
.hero .brand{position:absolute;top:30px;left:60px;color:var(--white)}
.hero .brand-dot{background:var(--blue-bright)}
.nav{position:absolute;top:58px;right:30px;display:flex;align-items:center;gap:30px;font-size:16px;font-weight:500;color:var(--white)}
.nav .portal{background:var(--white);color:var(--blue);padding:10px 18px;border-radius:4px;font-weight:600}
.nav .portal.dark{background:var(--blue);color:var(--white)}
.hero-copy{position:absolute;left:70px;top:350px;color:var(--white)}
.hero-copy h1{font-size:58px;font-weight:700;line-height:1.15;width:620px}
.hero-copy h1 em{font-style:normal;color:var(--blue-bright)}
.hero-copy p{font-size:20px;margin-top:14px;width:440px;line-height:1.45}
.hero-copy .actions{display:flex;gap:22px;margin-top:32px}
.hero-wave{position:absolute;left:0;bottom:0}
.hero-badge{position:absolute;left:560px;top:650px;width:80px;height:80px;border-radius:50%;background:var(--white);box-shadow:0 4px 16px rgba(0,0,0,.15);display:flex;align-items:center;justify-content:center}
.hero-badge i{width:44px;height:44px;border-radius:50%;background:var(--blue)}

/* SERVICES */
.services{height:800px;padding-top:20px}
.services .title{margin-top:8px}
.tabs{display:flex;justify-content:center;gap:16px;margin-top:50px}
.tab{height:48px;padding:0 22px;display:flex;align-items:center;gap:10px;font-size:15px;font-weight:500;border:1px solid var(--line);border-radius:4px;color:var(--text)}
.tab.active{background:var(--blue);color:var(--white);border-color:var(--blue)}
.services .lead{width:840px;margin:30px auto 0;text-align:center;font-size:16px;line-height:1.6}
.cards{display:flex;gap:28px;justify-content:center;margin-top:50px}
.card{width:252px;height:340px;background:var(--light);border-radius:6px;overflow:hidden;position:relative}
.card-photo{height:112px;background:linear-gradient(135deg,#93a9bf,#5f7a95)}
.card-icon{position:absolute;left:20px;top:86px;width:52px;height:52px;border-radius:4px;background:var(--white);display:flex;align-items:center;justify-content:center}
.card h3{font-size:22px;color:var(--blue);font-weight:600;margin:40px 0 8px 20px}
.card ul{list-style:none;margin-left:20px;font-size:14px;line-height:28px}
.card li::before{content:"✓";color:var(--blue);font-weight:700;margin-right:8px}
.card.featured{background:var(--navy);color:var(--white);height:360px;margin-top:-10px}
.card.featured h3{color:var(--white)}
.card.featured li::before{color:var(--white)}
.services .cta{display:flex;justify-content:center;margin-top:40px}

/* ABOUT */
.about{height:780px;background:linear-gradient(180deg,#16263f,#0d1b33)}
.about-top{position:absolute;top:0;left:0}
.about-photo{position:absolute;left:80px;top:150px;width:440px;height:520px;background:linear-gradient(135deg,#2a77c4,#123a66);clip-path:polygon(25% 0,75% 0,100% 50%,75% 100%,25% 100%,0 50%)}
.about-tag{position:absolute;left:70px;top:600px;width:170px;height:96px;background:var(--blue);clip-path:polygon(20% 0,80% 0,100% 50%,80% 100%,20% 100%,0 50%);color:var(--white);font-weight:600;font-size:15px;display:flex;align-items:center;justify-content:center;text-align:center}
.about-copy{position:absolute;left:560px;top:300px;width:560px;color:var(--white)}
.about-copy .eyebrow{text-align:left;color:var(--white)}
.about-copy h2{font-size:46px;font-weight:700;margin:6px 0 14px}
.about-copy p{font-size:15px;line-height:1.6;color:#c9d4e2}
.about-copy .btn{margin-top:26px}

/* WHY */
.why{height:640px}
.why .eyebrow{margin-top:70px}
.why-center{position:absolute;left:420px;top:220px;width:360px;height:360px;border-radius:50%;background:radial-gradient(circle,#6fa8d6,#1f5b92)}
.why-ring{position:absolute;left:400px;top:200px;width:400px;height:400px;border-radius:50%;border:2px dashed var(--line)}
.feature{position:absolute;display:flex;align-items:center;gap:18px;width:380px}
.feature.left{flex-direction:row-reverse;text-align:right}
.feature h4{font-size:20px;font-weight:600;color:var(--ink)}
.feature p{font-size:15px;color:var(--muted);margin-top:4px}
.feature .ico{flex:0 0 72px;height:72px;border-radius:50%;background:var(--blue);display:flex;align-items:center;justify-content:center}

/* REVIEWS */
.reviews{height:740px;background:linear-gradient(160deg,#0a5db0,#0d3d7a)}
.reviews .eyebrow{color:var(--white);margin-top:80px}
.reviews .title{color:var(--white)}
.review-row{display:flex;gap:40px;justify-content:center;margin-top:60px}
.review{width:300px;height:320px;background:var(--white);border-radius:6px;padding:26px;position:relative}
.quote{position:absolute;right:18px;top:-18px;width:44px;height:44px;border-radius:50%;background:var(--blue);color:var(--white);font-size:28px;font-weight:700;display:flex;align-items:center;justify-content:center}
.stars{color:var(--gold);font-size:20px;letter-spacing:2px}
.review p{font-size:15px;line-height:1.6;margin-top:10px;height:150px}
.reviewer{display:flex;align-items:center;gap:12px;border-top:1px solid var(--line);padding-top:16px;margin-top:14px}
.avatar{width:44px;height:44px;border-radius:50%;background:#aab8c8}
.reviewer b{display:block;font-size:14px;color:var(--ink)}
.reviewer small{font-size:13px;color:var(--muted)}
.arrow{position:absolute;top:470px;width:42px;height:42px;border-radius:50%;border:2px solid var(--white);display:flex;align-items:center;justify-content:center}

/* CONTACT */
.contact{height:660px;background:var(--white)}
.contact-shape{position:absolute;top:0;left:0}
.contact-copy{position:absolute;left:70px;top:180px;width:560px}
.contact-copy .eyebrow{text-align:left;color:var(--ink)}
.contact-copy h2{font-size:48px;font-weight:700;color:var(--blue)}
.form{display:grid;grid-template-columns:1fr 1fr;gap:16px;margin-top:30px}
.field{height:46px;border:1px solid var(--line);border-radius:4px;display:flex;align-items:center;gap:10px;padding:0 14px;font-size:14px;color:var(--muted)}
.field.area{grid-column:1/3;height:110px;align-items:flex-start;padding-top:14px}
.contact .btn{margin-top:22px}
.contact-photo{position:absolute;right:0;top:120px;width:520px;height:540px;background:linear-gradient(160deg,#b9cfe3,#4d6f91);clip-path:polygon(20% 0,100% 0,100% 100%,0 100%,0 40%)}

/* FOOTER */
.footer{height:488px;background:var(--ink);color:#c3cdd9}
.footer .brand{position:absolute;left:120px;top:80px;color:var(--white);flex-direction:column;gap:8px}
.footer .brand-dot{background:var(--blue-bright);width:52px;height:52px}
.socials{position:absolute;left:92px;top:200px;display:flex;gap:14px}
.socials i{width:34px;height:34px;border-radius:50%;border:1px solid #4b5a6e;display:block}
.fcol{position:absolute;top:90px}
.fcol h5{font-size:20px;color:var(--white);font-weight:600;margin-bottom:18px}
.fcol p,.fcol li{font-size:15px;line-height:30px;list-style:none}
.news-field{width:240px;height:44px;border-radius:4px;background:var(--white);margin-top:8px;display:flex;align-items:center;padding:0 14px;font-size:14px;color:var(--muted)}
.news .btn{margin-top:14px;height:44px;font-size:15px}
.copyright{position:absolute;bottom:0;left:0;right:0;height:80px;border-top:1px solid #223044;display:flex;align-items:center;justify-content:center;font-size:15px}
</style>
</head>
<body>

<header class="hero">
  <div class="hero-photo" role="img" aria-label="Technician in work gear cleaning rooftop solar panels"></div>
  <div class="topbar"><span>✉ sales@panelbrite.com.au</span><span>☎ Southern Highlands: (02) 4863 1507</span></div>
  <div class="brand"><span class="brand-dot"></span>PanelBrite</div>
  <nav class="nav">
    <span>Solar Cleaning</span><span>Gutter Cleaning</span><span>DustGuard</span><span>Contact</span>
    <span class="portal">Resellers Portal</span><span class="portal dark">Customer Portal</span>
  </nav>
  <div class="hero-copy">
    <h1>Premier <em>Solar</em> Panel Cleaning Services.</h1>
    <p>We have a detailed knowledge of the cleaning &amp; testing of Solar Panels.</p>
    <div class="actions"><span class="btn">Solar Cleaning ›</span><span class="btn">Gutter Cleaning ›</span></div>
  </div>
  <svg class="hero-wave" width="1200" height="200" viewBox="0 0 1200 200"><path d="M0 110 L470 200 L730 200 L1200 110 L1200 200 L0 200Z" fill="#fff"/><path d="M480 200 Q600 90 720 200Z" fill="#fff"/></svg>
  <div class="hero-badge"><i></i></div>
</header>

<section class="services">
  <p class="eyebrow">Who We Serve</p>
  <h2 class="title">Our Services</h2>
  <div class="tabs"><span class="tab active">☀ Solar Panel Cleaning</span><span class="tab">⌂ Gutter Cleaning</span></div>
  <p class="lead">We have a detailed knowledge of the cleaning &amp; testing of Solar Panels. Visual &amp; thermal check of your panels with report to you included in the price. We use only the best tools and LoftSuk cleaning systems.</p>
  <div class="cards">
    <div class="card"><div class="card-photo" role="img" aria-label="Government building"></div><div class="card-icon"><svg width="28" height="28" viewBox="0 0 28 28"><path d="M3 11 L14 4 L25 11Z M5 13h18v2H5Z M7 16h3v7H7Z M12.5 16h3v7h-3Z M18 16h3v7h-3Z M4 24h20v2H4Z" fill="#0a6fc2"/></svg></div><h3>Government</h3><ul><li>Detailed Knowledge</li><li>Visual &amp; Thermal Check</li><li>Best Cleaning Systems</li><li>Fully Equipped Staff</li><li>Trained and Insured</li></ul></div>
    <div class="card featured"><div class="card-photo" role="img" aria-label="Large solar farm infrastructure"></div><div class="card-icon"><svg width="28" height="28" viewBox="0 0 28 28"><rect x="4" y="8" width="20" height="14" fill="none" stroke="#0a6fc2" stroke-width="2"/><path d="M4 15h20M14 8v14" stroke="#0a6fc2" stroke-width="2"/></svg></div><h3>Infrastructure</h3><ul><li>Detailed Knowledge</li><li>Visual &amp; Thermal Check</li><li>Best Cleaning Systems</li><li>Fully Equipped Staff</li><li>Trained and Insured</li></ul></div>
    <div class="card"><div class="card-photo" role="img" aria-label="Commercial rooftop solar array"></div><div class="card-icon"><svg width="28" height="28" viewBox="0 0 28 28"><rect x="6" y="4" width="16" height="20" fill="none" stroke="#0a6fc2" stroke-width="2"/><path d="M10 9h3M15 9h3M10 14h3M15 14h3M12 24v-5h4v5" stroke="#0a6fc2" stroke-width="2"/></svg></div><h3>Commercial</h3><ul><li>Detailed Knowledge</li><li>Visual &amp; Thermal Check</li><li>Best Cleaning Systems</li><li>Fully Equipped Staff</li><li>Trained and Insured</li></ul></div>
    <div class="card"><div class="card-photo" role="img" aria-label="Residential house with roof solar panels"></div><div class="card-icon"><svg width="28" height="28" viewBox="0 0 28 28"><path d="M4 14 L14 5 L24 14 M7 12v11h14V12" fill="none" stroke="#0a6fc2" stroke-width="2"/></svg></div><h3>Residential</h3><ul><li>Detailed Knowledge</li><li>Visual &amp; Thermal Check</li><li>Best Cleaning Systems</li><li>Fully Equipped Staff</li><li>Trained and Insured</li></ul></div>
  </div>
  <div class="cta"><span class="btn">Request a Quote ›</span></div>
</section>

<section class="about">
  <svg class="about-top" width="1200" height="120" viewBox="0 0 1200 120"><path d="M0 0H1200V20L600 90 0 20Z" fill="#fff"/><path d="M0 20L600 90 1200 20" stroke="#0a6fc2" stroke-width="6" fill="none"/></svg>
  <div class="about-photo" role="img" aria-label="Smiling technician in hard hat with arms crossed"></div>
  <div class="about-tag">Professional<br>Cleaning</div>
  <div class="about-copy">
    <p class="eyebrow">Who We Are</p>
    <h2>About PanelBrite</h2>
    <p>We are a family run team servicing homes, schools, councils and solar farms across the region. Our crews are trained, insured and fully equipped to clean and test panels of every size. We check each system visually and with thermal imaging, then send a clear report so you know exactly how your panels perform. From a single roof to a field of a million panels, we bring the same care, safety and attention to detail to every job we take on, every time.</p>
    <span class="btn">Read More ›</span>
  </div>
</section>

<section class="why">
  <p class="eyebrow">Why Choose Us</p>
  <h2 class="title">Why Clean Your Panels</h2>
  <div class="why-ring"></div>
  <div class="why-center" role="img" aria-label="Rotary brush cleaning a solar panel, seen from above"></div>
  <div class="feature left" style="left:40px;top:260px"><span class="ico"><svg width="34" height="34" viewBox="0 0 34 34"><path d="M6 24l8-8 6 5 8-10" stroke="#fff" stroke-width="3" fill="none"/></svg></span><div><h4>Increased Efficiency</h4><p>Maintain and increase the efficiency of your panels</p></div></div>
  <div class="feature left" style="left:40px;top:430px"><span class="ico"><svg width="34" height="34" viewBox="0 0 34 34"><path d="M17 5l10 4v8c0 6-4 10-10 12-6-2-10-6-10-12V9Z" stroke="#fff" stroke-width="3" fill="none"/></svg></span><div><h4>Maintain Warranty</h4><p>Maintain Warranty Obligations</p></div></div>
  <div class="feature" style="left:780px;top:260px"><span class="ico"><svg width="34" height="34" viewBox="0 0 34 34"><path d="M19 4L9 19h8l-2 11 10-15h-8Z" fill="#fff"/></svg></span><div><h4>Increase Power Output</h4><p>Increase energy output by 20% or more</p></div></div>
  <div class="feature" style="left:780px;top:430px"><span class="ico"><svg width="34" height="34" viewBox="0 0 34 34"><circle cx="17" cy="17" r="11" stroke="#fff" stroke-width="3" fill="none"/><path d="M11 23L23 11" stroke="#fff" stroke-width="3"/></svg></span><div><h4>No Contact Covid Safe</h4><p>We use a contactless and Covid safe system</p></div></div>
</section>

<section class="reviews">
  <p class="eyebrow">Testimonials</p>
  <h2 class="title">Customer Reviews</h2>
  <span class="arrow" style="left:40px"><svg width="16" height="16" viewBox="0 0 16 16"><path d="M10 3L5 8l5 5" stroke="#fff" stroke-width="2" fill="none"/></svg></span>
  <span class="arrow" style="right:40px"><svg width="16" height="16" viewBox="0 0 16 16"><path d="M6 3l5 5-5 5" stroke="#fff" stroke-width="2" fill="none"/></svg></span>
  <div class="review-row">
    <div class="review"><span class="quote">”</span><div class="stars">★★★★★</div><p>Another excellent service from PanelBrite. Arrived on time and completed the job well. Easy to deal with and great technician. We will have them again.</p><div class="reviewer"><span class="avatar"></span><div><b>MARCUS TELLEN</b><small>12 December 2024</small></div></div></div>
    <div class="review"><span class="quote">”</span><div class="stars">★★★★★</div><p>This is the third year the guys from PanelBrite have cleaned my gutters and I am very happy to recommend them. My job is not an easy one, double story. <span style="color:var(--blue)">Read More</span></p><div class="reviewer"><span class="avatar"></span><div><b>DEAN FARROW</b><small>6 December 2024</small></div></div></div>
    <div class="review"><span class="quote">”</span><div class="stars">★★★★★</div><p>Amazing job cleaning out my gutters. It was sunny and very hot. Definitely a lot more dirt in the gutters than I expected and a lot of extra work but <span style="color:var(--blue)">Read More</span></p><div class="reviewer"><span class="avatar"></span><div><b>TOM R</b><small>5 December 2024</small></div></div></div>
  </div>
</section>

<section class="contact">
  <svg class="contact-shape" width="1200" height="200" viewBox="0 0 1200 200"><path d="M0 0H1200V60L600 160 0 60Z" fill="#0d3d7a"/><path d="M0 60L600 160 1200 60" stroke="#0a6fc2" stroke-width="6" fill="none"/></svg>
  <div class="contact-copy">
    <p class="eyebrow">Get In Touch</p>
    <h2>Contact Us</h2>
    <div class="form">
      <span class="field">👤 First Name</span><span class="field">👤 Last Name</span>
      <span class="field">☎ Phone Number</span><span class="field">✉ Email Address</span>
      <span class="field area">✎ Leave message</span>
    </div>
    <span class="btn">Send Message ›</span>
  </div>
  <div class="contact-photo" role="img" aria-label="Worker in hard hat washing solar panels with a long brush"></div>
</section>

<footer class="footer">
  <div class="brand"><span class="brand-dot"></span>PanelBrite</div>
  <div class="socials"><i></i><i></i><i></i><i></i></div>
  <div class="fcol" style="left:360px"><h5>Quick Links</h5><ul><li>Solar Cleaning</li><li>Gutter Cleaning</li><li>DustGuard</li><li>Contact</li></ul></div>
  <div class="fcol" style="left:580px"><h5>Contact Info</h5><p>📍 14/22 Wattle Close,<br>&nbsp;&nbsp;&nbsp;&nbsp;Ferndell NSW 2583</p><p style="margin-top:20px">✉ sales@panelbrite.com.au</p></div>
  <div class="fcol news" style="left:880px"><h5>Newsletter For Updates</h5><div class="news-field">✉ Email Address</div><span class="btn">Subscribe Now ›</span></div>
  <div class="copyright">© 2025 PanelBrite. All Rights Reserved.</div>
</footer>

</body>
</html>
```